8'x8' Exhibit Backdrop for Healthcare Events focused on the 55 and older crowds

8X8 Backdrop for Exhibiting.

I also want a design for a 6' table skirt to include our logo on two sides and the logo with Hereditary Cancer Screening underneath on the front. I want the main message of Will You Give your Loved Ones The Information To Beat Cancer in Their Lives to be completely centered on the 8X8 backdrop. Hereditary Cancer Screening The Test You Take For Them in the top left corner and the purple box on the right hand side - just like the photo that has been uploaded below. I need High resolution photos around the backdrop but not so large that they overtake the main message.

Target Market(s)

55+ crowd living in Adult only communities. They have an active lifestyle

Industry/Entity Type

Healthcare

Other font styles liked:
• "The Test You Take For Them" is Comic Sans

Colors
0255a3
fbed22
ffffff

Requirements
Must have
• I am posting a photo of the exact backdrop I would like to see. There are red arrows showing where to move certain items. There is a space underneath the slogan WILL YOU GIVE YOUR LOVED ONES... where another photo will go. Add another photo underneath the slogan that you are moving up - GIVE THEM THE GIFT OF KNOWLEDGE
• See the upload section for the new photo
• Do this one exactly like I am asking for and then you can show me some of your ideas. Thanks
• THE PHOTOS UPLOADED ARE EXAMPLES. FEEL FREE TO SEARCH OUT YOUR OWN HIGH RESOLUTION PHOTOS. THANKS

```html
<!DOCTYPE html>
<html lang="en">
<head>
<meta charset="utf-8">
<title>Hereditary Cancer Screening – Exhibit Backdrop</title>
<link rel="stylesheet" href="https://fonts.googleapis.com/css2?family=Bebas+Neue&family=Montserrat:wght@400;600;700&family=Oswald:wght@200;300&family=Open+Sans:wght@400&display=swap">
<style>
  :root {
    --navy: #111a5b;
    --navy-deep: #0b1150;
    --green: #8dc04a;
    --white: #ffffff;
  }
  html, body { margin: 0; padding: 0; overflow: hidden; background: var(--white); }
  .backdrop {
    position: relative;
    width: 1200px;
    height: 1200px;
    overflow: hidden;
    background: var(--white);
    font-family: "Montserrat", sans-serif;
  }
  .title {
    position: absolute;
    left: 49px;
    top: 36px;
    margin: 0;
    color: var(--navy);
    font-size: 59px;
    line-height: 52px;
    font-weight: 400;
    letter-spacing: -0.5px;
  }
  .title strong { font-weight: 700; display: block; }
  .title span { display: block; }
  .tagline {
    position: absolute;
    left: 49px;
    top: 220px;
    width: 294px;
    height: 34px;
    background: var(--green);
    color: var(--white);
    font-size: 20px;
    font-weight: 400;
    line-height: 34px;
    text-align: center;
  }
  .photo { position: absolute; }
  .photo-1 { left: 0; top: 276px; width: 234px; height: 160px; background: linear-gradient(135deg, #6b5a2a, #1d1a14 70%); }
  .photo-2 { left: 247px; top: 276px; width: 236px; height: 160px; background: linear-gradient(135deg, #6d6f6a, #3a3b38); }
  .photo-3 { left: 498px; top: 278px; width: 233px; height: 158px; background: linear-gradient(135deg, #e6ded6, #cfc2bb); }
  .photo-4 { left: 751px; top: 278px; width: 234px; height: 158px; background: linear-gradient(135deg, #ece6e2, #b9a89a); }
  .photo-5 { left: 995px; top: 278px; width: 205px; height: 158px; background: linear-gradient(135deg, #b2702e, #4a3a36); }
  .photo-hero { left: 0; top: 449px; width: 415px; height: 327px; background: linear-gradient(135deg, #8fa34a, #c9b9a6 55%, #7e9ac4); }
  .panel {
    position: absolute;
    left: 774px;
    top: 446px;
    width: 426px;
    height: 754px;
    background: var(--navy-deep);
  }
  .panel-photo {
    position: absolute;
    left: 0; top: 0;
    width: 426px; height: 330px;
    background: linear-gradient(180deg, #4f56a3, #2d3580 60%, var(--navy-deep));
  }
  .slogan {
    position: absolute;
    left: 448px;
    top: 458px;
    width: 292px;
    color: var(--navy);
    font-family: "Bebas Neue", sans-serif;
  }
  .slogan .line { display: block; text-align: center; white-space: nowrap; }
  .line-give { font-size: 54px; line-height: 76px; height: 76px; }
  .line-give b { font-weight: 400; font-size: 96px; }
  .line-loved { font-size: 55px; line-height: 48px; }
  .line-info {
    margin: 2px 0 0 0;
    background: var(--navy);
    color: var(--white);
    font-family: "Oswald", sans-serif;
    font-weight: 300;
    font-size: 27px;
    line-height: 34px;
    letter-spacing: -0.6px;
  }
  .line-cancer { color: var(--green); font-size: 124px; line-height: 108px; letter-spacing: -1px; }
  .line-lives { font-size: 64px; line-height: 56px; }
  .gift {
    position: absolute;
    right: 30px;
    top: 848px;
    margin: 0;
    color: var(--white);
    text-align: right;
  }
  .gift span { display: block; white-space: nowrap; }
  .gift-head { font-family: "Bebas Neue", sans-serif; font-size: 70px; line-height: 58px; }
  .gift-head em { font-style: normal; font-family: "Oswald", sans-serif; font-weight: 200; font-size: 60px; }
  .gift-sub { font-family: "Oswald", sans-serif; font-weight: 200; font-size: 46px; line-height: 44px; }
  .gift-key { font-family: "Bebas Neue", sans-serif; font-size: 76px; line-height: 62px; }
  .gift-note { font-family: "Open Sans", sans-serif; font-size: 32px; line-height: 38px; }
  .brand {
    position: absolute;
    left: 36px;
    top: 1040px;
    display: flex;
    align-items: center;
    gap: 18px;
  }
  .brand-dot { width: 120px; height: 120px; border-radius: 50%; background: var(--navy); }
  .brand-name {
    color: var(--navy);
    font-family: "Montserrat", sans-serif;
    font-weight: 600;
    font-size: 36px;
    line-height: 40px;
    letter-spacing: 1px;
  }
</style>
</head>
<body>
<main class="backdrop">
  <h1 class="title"><strong>Hereditary</strong><span>Cancer</span><span>Screening</span></h1>
  <div class="tagline">The Test You Take For Them</div>

  <div class="photo photo-1" role="img" aria-label="Older men playing chess outdoors in autumn light"></div>
  <div class="photo photo-2" role="img" aria-label="Senior couple dancing in a loft"></div>
  <div class="photo photo-3" role="img" aria-label="Grandmother, mother and daughter on a sofa with tea"></div>
  <div class="photo photo-4" role="img" aria-label="Three-generation family sitting together smiling"></div>
  <div class="photo photo-5" role="img" aria-label="Senior couple at a swing in an autumn garden"></div>
  <div class="photo photo-hero" role="img" aria-label="Woman kissing a smiling senior man outdoors"></div>

  <div class="slogan">
    <span class="line line-give">Will you <b>Give</b></span>
    <span class="line line-loved">Your loved ones</span>
    <span class="line line-info">THE INFORMATION TO BEAT</span>
    <span class="line line-cancer">Cancer</span>
    <span class="line line-lives">In their lives?</span>
  </div>

  <section class="panel">
    <div class="panel-photo" role="img" aria-label="Grandfather with grandson hugging him from behind, tinted blue"></div>
  </section>

  <p class="gift">
    <span class="gift-head">Give <em>THEM</em></span>
    <span class="gift-sub">THE GIFT OF</span>
    <span class="gift-key">Knowledge</span>
    <span class="gift-note">that you will be</span>
    <span class="gift-note">moving up.</span>
  </p>

  <div class="brand">
    <div class="brand-dot"></div>
    <div class="brand-name">KINDRED<br>HEALTH<br>GROUP</div>
  </div>
</main>
</body>
</html>
```